New Summit Tile Billboard at HQ

Looking to design a catchy image / theme for a billboard located just above our corporate HQ showroom and warehouse, along the service road of a 6-lane highway. Billboard measures 8ft x 24 ft. Would like to highlight that the store location is directly beneath the sign.

We are a retail and wholesale business selling premium flooring, ready to assemble cabinets, and granite countertops. See image ideas attached. Our information:
NAME: Summit Tile, Cabinets, Countertops
ADDRESS: 417 W. Hwy 82, Duncanville, TX 75284
WEBSITE: www.summittilehub.example
PHONE: 972-8-TILEUP (972-845-3887)

```html
<!DOCTYPE html>
<html lang="en">
<head>
<meta charset="utf-8">
<title>Summit Tile Billboard</title>
<link rel="stylesheet" href="https://fonts.googleapis.com/css2?family=Anton&family=Montserrat:wght@600;700&display=swap">
<style>
  :root {
    --page-bg: #ffffff;
    --lime: #7fc52f;
    --charcoal: #262626;
    --signal-red: #ee2024;
    --paper: #f6f6f4;
    --ink: #111111;
    --white: #ffffff;
    --slab-light: #9a9c96;
    --slab-dark: #5e6461;
  }
  html, body {
    margin: 0;
    padding: 0;
    width: 800px;
    height: 1200px;
    overflow: hidden;
    background: var(--page-bg);
  }
  .canvas {
    position: relative;
    width: 800px;
    height: 1200px;
  }
  .billboard {
    position: absolute;
    left: 30px;
    top: 476px;
    width: 740px;
    height: 247px;
    background: var(--paper);
    box-shadow: 2px 3px 6px rgba(0,0,0,0.35);
    overflow: hidden;
  }
  .billboard-shapes {
    position: absolute;
    inset: 0;
  }
  .offer-list {
    position: absolute;
    left: 22px;
    top: 24px;
    display: flex;
    gap: 5px;
    font-family: "Montserrat", sans-serif;
    font-weight: 700;
    font-size: 13px;
    line-height: 1;
  }
  .offer-list span {
    background: var(--white);
    color: var(--ink);
    padding: 3px 4px 3px 3px;
  }
  .headline {
    position: absolute;
    left: 20px;
    top: 44px;
    margin: 0;
    font-family: "Anton", sans-serif;
    font-weight: 400;
    font-size: 46px;
    line-height: 1.1;
    color: var(--signal-red);
    letter-spacing: 0.5px;
  }
  .contact-lines {
    position: absolute;
    left: 22px;
    top: 111px;
    font-family: "Montserrat", sans-serif;
    font-weight: 600;
    font-size: 17px;
    line-height: 23px;
    color: var(--ink);
  }
  .contact-line {
    display: flex;
    align-items: center;
    gap: 6px;
    white-space: nowrap;
  }
  .contact-line.indent { padding-left: 20px; }
  .contact-line svg { width: 14px; height: 14px; flex: none; }
  .phone-line {
    position: absolute;
    left: 22px;
    top: 206px;
    display: flex;
    align-items: center;
    gap: 8px;
    font-family: "Anton", sans-serif;
    font-size: 21px;
    line-height: 30px;
    color: var(--white);
    letter-spacing: 0.3px;
  }
  .phone-line svg { width: 17px; height: 17px; }
  .location-callout {
    position: absolute;
    left: 324px;
    top: 106px;
    font-family: "Anton", sans-serif;
    font-size: 25px;
    line-height: 29px;
    color: var(--lime);
    letter-spacing: 0.3px;
    text-shadow:
      1px 0 0 var(--white), -1px 0 0 var(--white),
      0 1px 0 var(--white), 0 -1px 0 var(--white),
      1px 1px 0 var(--white), -1px -1px 0 var(--white),
      1px -1px 0 var(--white), -1px 1px 0 var(--white);
  }
  .brand-name {
    position: absolute;
    right: 22px;
    top: 46px;
    display: flex;
    align-items: center;
    gap: 8px;
    font-family: "Montserrat", sans-serif;
    font-weight: 700;
    font-size: 24px;
    line-height: 1;
    color: var(--ink);
    white-space: nowrap;
  }
  .brand-name .brand-square {
    width: 22px;
    height: 22px;
    background: var(--lime);
  }
</style>
</head>
<body>
<div class="canvas">
  <section class="billboard" aria-label="Summit Tile billboard">
    <svg class="billboard-shapes" viewBox="0 0 740 247" width="740" height="247">
      <defs>
        <linearGradient id="slabTone" x1="0" y1="0" x2="1" y2="1">
          <stop offset="0" stop-color="#9a9c96"/>
          <stop offset="1" stop-color="#5e6461"/>
        </linearGradient>
      </defs>
      <rect class="lifestyle-photo" x="432" y="112" width="302" height="120" rx="4" fill="url(#slabTone)" role="img" aria-label="Photo of a person relaxing with a tablet on a large stone tile slab"/>
      <polygon class="green-panel" points="0,0 438,0 400,197 0,197" fill="var(--lime)"/>
      <polygon class="phone-band" points="0,197 400,197 380,247 0,247" fill="var(--charcoal)"/>
      <polygon class="down-arrow" points="380,36 451,53 418,198 438,209 374,247 327,187 357,181"
               fill="var(--signal-red)" stroke="var(--charcoal)" stroke-width="3" stroke-linejoin="round"/>
    </svg>

    <div class="offer-list">
      <span>FLOORS,</span><span>CABINETS,</span><span>COUNTERTOPS</span>
    </div>

    <h1 class="headline">NEED FLOORING?</h1>

    <div class="contact-lines">
      <div class="contact-line">
        <svg viewBox="0 0 24 24" aria-hidden="true"><path d="M12 2a7 7 0 0 0-7 7c0 5 7 13 7 13s7-8 7-13a7 7 0 0 0-7-7zm0 9.5A2.5 2.5 0 1 1 12 6.5a2.5 2.5 0 0 1 0 5z" fill="#111111"/></svg>
        417 W. Hwy 82,
      </div>
      <div class="contact-line indent">Duncanville, TX 75284</div>
      <div class="contact-line">
        <svg viewBox="0 0 24 24" aria-hidden="true"><circle cx="12" cy="12" r="9" fill="none" stroke="#111111" stroke-width="2"/><path d="M3 12h18M12 3c3 3 3 15 0 18M12 3c-3 3-3 15 0 18" fill="none" stroke="#111111" stroke-width="1.6"/></svg>
        www.summittilehub.example
      </div>
    </div>

    <div class="phone-line">
      <svg viewBox="0 0 24 24" aria-hidden="true"><circle cx="12" cy="12" r="11" fill="#7fc52f"/><path d="M8.5 6.5l2 2.5-1.2 1.4c.8 1.7 2 2.9 3.6 3.7l1.4-1.2 2.5 2-1 2c-4.4-.3-8.2-4.1-8.5-8.5z" fill="#ffffff"/></svg>
      972-8-TILEUP (972-845-3887)
    </div>

    <div class="location-callout">RIGHT HERE<br>RIGHT NOW</div>

    <div class="brand-name"><span class="brand-square"></span>Summit Tile</div>
  </section>
</div>
</body>
</html>
```